Labels for a Supplement Detox Kit( 2 products in a kit)

I have 2 products a (dropper bottle (30ml) Liquid and jar(120g Powder)) that are sold as a kit . They cannot be purchased separately I need labels for this set.
Norvanta is a wellness company that specialises in health and wellness products. Formulated by a nutritionist and herbalist. These products are aimed at detoxing the gut . My logo is gold would like to see the design in black or gold with hints of dark burgundy to match the overall brand.

Target Market(s)

25-50

Industry/Entity Type

Health & Wellness

Requirements
Must have
• Description and ingredients on there
Nice to have
• I would like a shape or design behind the label
Should not have
• Not too many colours or designs - need simple and clear

```html
<!DOCTYPE html>
<html lang="en">
<head>
<meta charset="utf-8">
<title>Norvanta Gut Cleanse Labels</title>
<link rel="stylesheet" href="https://fonts.googleapis.com/css2?family=Lexend:wght@300;400&display=swap">
<style>
:root{
  --page:#f5f5f5;
  --black:#050505;
  --panel:#dcdcdc;
  --white:#efefef;
  --gold:#c9971f;
  --gold-light:#f7dc5c;
  --gold-dark:#b7841a;
  --burgundy:#6a1a2a;
  --burgundy-dark:#561322;
  --ink:#111;
}
*{box-sizing:border-box;margin:0;padding:0}
html,body{width:1102px;height:1200px;overflow:hidden;background:var(--page);font-family:"Lexend",sans-serif;font-weight:300;color:var(--ink)}
.canvas{position:relative;width:1102px;height:1200px}
.abs{position:absolute}

/* flat wrap label */
.wrap-label{left:42px;top:74px;width:1016px;height:224px;background:var(--black)}
.wrap-label .sheen{left:0;top:70px;width:100%;height:19px;background:linear-gradient(#1a1a1a,#6a6a6a 30%,#3a3a3a 70%,#111)}
.wrap-label .bottom{left:0;top:206px;width:100%;height:18px;background:var(--black)}
.panel{top:89px;height:117px;background:var(--panel)}
.panel-left{left:0;width:303px}
.panel-center{left:303px;width:391px;background:var(--white)}
.panel-right{left:694px;width:322px}
.rule{width:1px;background:var(--gold);top:6px;height:104px}
.small-head{color:var(--gold);font-size:6.4px;letter-spacing:.1px;margin-bottom:1px}
.small-text{font-size:6px;line-height:8.2px}
.small-gold{color:var(--gold);font-size:6px;line-height:8.2px;margin-top:5px}

.wordmark{color:var(--gold);font-weight:300;text-align:center;letter-spacing:1px}
.nutra-band{background:linear-gradient(90deg,var(--gold-dark),var(--gold-light) 50%,var(--gold-dark));color:var(--burgundy);text-align:center;font-weight:400}
.title-box{background:var(--burgundy);color:var(--gold-light)}
.desc{color:var(--burgundy);font-weight:400}

/* bottles */
.dropper-tip{width:44px;height:86px;border-radius:22px 22px 0 0;background:linear-gradient(90deg,#0a0a0a,#2a2a2a 40%,#0a0a0a)}
.dropper-cap{width:132px;height:103px;background:linear-gradient(90deg,#111,#3b3b3b 45%,#111)}
.bottle-body{width:238px;height:567px;border-radius:119px 119px 0 0/110px 110px 0 0;background:linear-gradient(90deg,#0a0a0a,#2e2e2e 45%,#060606)}
.front-label{width:180px;height:472px;border-radius:90px 90px 0 0/72px 72px 0 0;background:linear-gradient(180deg,#fff,#ececec);overflow:hidden;text-align:center}
.back-label{width:180px;height:472px;border-radius:90px 90px 0 0/72px 72px 0 0;background:var(--panel);overflow:hidden;text-align:center}
.back-label .block{padding:0 6px}
.back-head{color:var(--gold);font-size:8.4px;margin-top:10px}
.back-text{font-size:8.2px;line-height:9.8px}
.back-gold{color:var(--gold);font-size:8.2px;line-height:9.8px;margin-top:10px}
</style>
</head>
<body>
<div class="canvas">

  <section class="abs wrap-label" aria-label="Wrap-around label">
    <div class="abs sheen"></div>

    <div class="abs panel panel-left">
      <div class="abs rule" style="left:18px"></div>
      <div class="abs" style="left:31px;top:6px;width:100px">
        <p class="small-head">SUGGESTED USAGE</p>
        <p class="small-text">1-3 drops, 1 time per day or as directed. To decrease detoxification reactions, increase very gradually from 1 drop a day up to 3 drops one time a day or as directed by a healthcare professional. Not for use during pregnancy. Ask your healthcare professional when starting any new supplement.</p>
      </div>
      <div class="abs rule" style="left:144px"></div>
      <div class="abs" style="left:156px;top:6px;width:128px">
        <p class="small-head">WARNING</p>
        <p class="small-text">Do not use during pregnancy. Consult your physician before using any supplement especially if you are nursing have a medical condition or if you are taking a medication. Discontinue use should adverse effects occur. Keep out of reach of children.</p>
        <p class="small-gold">Store in a cool dry place<br>Shake well before use</p>
      </div>
    </div>

    <div class="abs panel panel-center">
      <p class="abs wordmark" style="left:20px;top:60px;width:120px;font-size:20px">Norvanta</p>
      <p class="abs nutra-band" style="left:40px;top:92px;width:93px;height:17px;font-size:8.5px;line-height:17px">NUTRACEUTICALS</p>
      <div class="abs title-box" style="left:155px;top:0;width:195px;height:73px">
        <svg class="abs" style="left:0;top:0" width="195" height="73" viewBox="0 0 195 73" aria-hidden="true">
          <defs><linearGradient id="gold-a" x1="0" y1="0" x2="1" y2="1"><stop offset="0" stop-color="#f7dc5c"/><stop offset=".55" stop-color="#e3b43a"/><stop offset="1" stop-color="#b7841a"/></linearGradient></defs>
          <polygon points="140,0 195,0 195,73 158,73 150,45" fill="url(#gold-a)"/>
        </svg>
        <p class="abs" style="left:14px;top:5px;font-size:16px;line-height:21px">Anti-Microbial<br>Botanical<br>Gut Cleanse</p>
        <p class="abs" style="left:153px;top:47px;font-size:15px;color:var(--burgundy)">120g</p>
      </div>
      <p class="abs desc" style="left:155px;top:81px;width:230px;font-size:9.4px;line-height:12px">Proprietary blend of professional strength botanical extracts and essential oils to target pathogenic overgrowth</p>
    </div>

    <div class="abs panel panel-right">
      <div class="abs rule" style="left:0"></div>
      <div class="abs" style="left:31px;top:6px;width:200px">
        <p class="small-head">HERBAL BLEND INGREDIENTS</p>
        <p class="small-text">Vegetable Glycerine<br>Olive Leaf (Olea Europaea)<br>Black Cumin Seed (Nigella Sativa)<br>Neem (Azadirachta Seed)<br>Wormwood (Artemisia Absinthium)<br>Black Walnut (Juglans Nigra) hulls and leaves<br>Oregano (Origanum Vulgare leaf extract 30% carvacrol)<br>Cloves (Syzygium Aromaticum)<br>Ginger Bitters<br>Gentian (Gentiana Lutea Root Extract<br>Grapeseed (Vitis Vinifera Seed Extract)<br>Peppermint (Mentha Piperita)</p>
      </div>
    </div>
    <div class="abs bottom"></div>
  </section>

  <!-- front bottle -->
  <section aria-label="Dropper bottle, front">
    <div class="abs dropper-tip" style="left:350px;top:367px"></div>
    <div class="abs dropper-cap" style="left:306px;top:446px"></div>
    <div class="abs bottle-body" style="left:253px;top:548px"></div>
    <div class="abs front-label" style="left:282px;top:608px">
      <p class="abs wordmark" style="left:0;top:118px;width:180px;font-size:28px">Norvanta</p>
      <p class="abs nutra-band" style="left:0;top:158px;width:180px;height:30px;font-size:14px;line-height:30px">NUTRACEUTICALS</p>
      <svg class="abs" style="left:0;top:188px" width="180" height="143" viewBox="0 0 180 143" aria-hidden="true">
        <polygon points="0,0 180,0 180,130 90,143 0,130" fill="#6a1a2a"/>
      </svg>
      <p class="abs" style="left:0;top:211px;width:180px;color:var(--gold-light);font-size:22px;line-height:29px">Anti-Microbial<br>Botanical<br>Gut Cleanse</p>
      <p class="abs desc" style="left:6px;top:341px;width:168px;font-size:12.6px;line-height:14.6px">Proprietary blend<br>of professional strength<br>botanical extracts<br>and essential oils<br>to target pathogenic<br>overgrowth</p>
      <p class="abs nutra-band" style="left:0;top:442px;width:180px;height:30px;font-size:15px;line-height:30px;font-weight:300">1 fl oz (30ml)</p>
    </div>
  </section>

  <!-- back bottle -->
  <section aria-label="Dropper bottle, back">
    <div class="abs dropper-tip" style="left:708px;top:367px"></div>
    <div class="abs dropper-cap" style="left:664px;top:446px"></div>
    <div class="abs bottle-body" style="left:611px;top:548px"></div>
    <div class="abs back-label" style="left:640px;top:608px">
      <div class="block" style="margin-top:30px">
        <p class="back-head" style="margin-top:0">HERBAL BLEND INGREDIENTS</p>
        <p class="back-text">Vegetable Glycerine, Olive Leaf (Olea Europaea), Black Cumin Seed (Nigella Sativa), Neem (Azadirachta Seed), Wormwood (Artemisia Absinthium), Black Walnut (Juglans Nigra) hulls and leaves, Oregano (Origanum Vulgare leaf extract 30% carvacrol), Cloves (Syzygium Aromaticum), Ginger Bitters, Gentian (Gentiana Lutea Root Extract), Grapeseed (Vitis Vinifera Seed Extract), Peppermint (Mentha Piperita)</p>
        <p class="back-head">SUGGESTED USAGE</p>
        <p class="back-text">1-3 drops, 1 time per day or as directed. To decrease detoxification reactions, increase very gradually from 1 drop a day up to 3 drops one time a day or as directed by a healthcare professional. Not for use during pregnancy. Ask your healthcare professional when starting any new supplement.</p>
        <p class="back-head">WARNING</p>
        <p class="back-text">Do not use during pregnancy. Consult your physician before using any supplement especially if you are nursing have a medical condition or if you are taking a medication. Discontinue use should adverse effects occur. Keep out of reach of children.</p>
        <p class="back-gold">Store in a cool dry place<br>Shake well before use</p>
      </div>
      <div class="abs nutra-band" style="left:0;top:441px;width:180px;height:31px"></div>
    </div>
  </section>

</div>
</body>
</html>
```